Serene Mind-Rest: Quiet Hour Now, Inc.
Create business card, stationery, envelope design
Professional
Marisol T. Okafor, RN, MSN
Founder/Director
712 Harrowgate Lane, Suite PK3
Brooklyn, New York 11347
Marisol@Quiethournow.com
www.Quiethournow.com
Please use the following pantone colors:
purple [266], blue [279] and yellow [123]
Use purple [266] for font on back of card
Guiding Others Toward Calm
Empowering Others Is ~ Serene Mind-Rest: Quiet Hour Now
Serene Mind-Rest: Quiet Hour Now ~ Is Loving Myself®™
Hello Designers,
I uploaded my current business card so that you can see what I have already.
I just realized after comparing both cards, I did not add my roles on the business card project!
Please add:
Self-Care Specialist
Holistic Nurse Educator
Certified Wellness Coach/Speaker
Thank you,
Marisol

```html
<!DOCTYPE html>
<html lang="en">
<head>
<meta charset="utf-8">
<title>Serene Mind-Rest: Quiet Hour Now, Inc. — Stationery</title>
<link href="https://fonts.googleapis.com/css2?family=Libre+Baskerville:wght@400;700&display=swap" rel="stylesheet">
<style>
:root{
  --purple:#6a4a9e;
  --blue:#418fde;
  --yellow:#ffc72c;
  --ink:#2b2b33;
  --paper:#ffffff;
  --stage:#ffffff;
  --fold:#9a9aa2;
  --shadow:rgba(0,0,0,.28);
}
*{box-sizing:border-box;margin:0;padding:0}
html,body{width:1200px;height:681px;overflow:hidden;background:var(--stage)}
body{position:relative;font-family:"Libre Baskerville",Georgia,serif;color:var(--ink)}
.piece{position:absolute;background:var(--paper);box-shadow:2px 3px 7px var(--shadow);overflow:hidden}
.band{position:absolute;left:0;top:0;width:100%;display:block}
.brand{display:flex;align-items:center;gap:6px}
.brand-dot{flex:none;border-radius:50%;background:var(--yellow)}
.brand-name{color:var(--purple);font-weight:700;line-height:1.2}
.tagline{color:var(--purple);font-size:6.5px;margin-top:3px}
.address{font-size:7.5px;line-height:1.5;font-weight:700}

.envelope-front{left:60px;top:115px;width:432px;height:197px}
.envelope-front .brand-block{position:absolute;left:18px;top:44px;width:200px}
.envelope-front .brand{flex-direction:column;align-items:flex-start;gap:4px}
.envelope-front .brand-dot{width:18px;height:18px;margin-left:30px}
.envelope-front .brand-name{font-size:11px}
.envelope-front .address{margin-top:10px}

.envelope-back{left:60px;top:365px;width:432px;height:201px}
.envelope-back .flap{position:absolute;inset:0;width:100%;height:100%}
.envelope-back .brand{position:absolute;left:50%;top:76px;transform:translateX(-50%);flex-direction:column;gap:5px;text-align:center;width:180px}
.envelope-back .brand-dot{width:26px;height:26px}
.envelope-back .brand-name{font-size:9px}

.letterhead{left:620px;top:48px;width:330px;height:581px}
.letterhead .brand-block{position:absolute;left:22px;top:60px;width:200px}
.letterhead .brand{flex-direction:column;align-items:flex-start;gap:6px}
.letterhead .brand-dot{width:28px;height:28px;margin-left:56px}
.letterhead .brand-name{font-size:11px}
.letterhead .address{margin-top:10px}

.card-front{left:967px;top:115px;width:195px;height:115px}
.card-front .brand-block{position:absolute;left:10px;top:28px;width:82px}
.card-front .brand{flex-direction:column;align-items:flex-start;gap:3px}
.card-front .brand-dot{width:12px;height:12px;margin-left:16px}
.card-front .brand-name{font-size:6.5px}
.card-front .tagline{font-size:4px}
.card-front .contact{position:absolute;right:8px;top:10px;width:92px;text-align:right;font-size:5px;line-height:1.5}
.card-front .contact .person{font-weight:700;font-size:5.5px}
.card-front .contact .roles{color:var(--purple);margin:2px 0}
.card-front .address{font-size:5px;position:absolute;left:10px;bottom:12px}

.card-back{left:967px;top:242px;width:195px;height:113px;background:var(--purple)}
.card-back .mark{position:absolute;left:50%;top:18px;width:34px;height:34px;margin-left:-17px;border-radius:50%;background:var(--paper)}
.card-back .lines{position:absolute;left:20px;right:20px;top:62px;color:var(--paper);font-size:5px;line-height:1.6;text-align:center}
</style>
</head>
<body>

<section class="piece envelope-front" aria-label="Envelope front">
  <svg class="band" viewBox="0 0 432 36" height="36" preserveAspectRatio="none">
    <path d="M0 0H432V6Q270 28 0 26Z" fill="var(--purple)"/>
    <path d="M0 29Q270 31 432 9" fill="none" stroke="var(--blue)" stroke-width="2"/>
  </svg>
  <div class="brand-block">
    <div class="brand"><span class="brand-dot"></span><span class="brand-name">Serene Mind-Rest: Quiet Hour Now</span></div>
    <p class="tagline">Guiding Others Toward Calm</p>
    <p class="address">712 Harrowgate Lane, Suite PK3<br>Brooklyn, New York 11347</p>
  </div>
</section>

<section class="piece envelope-back" aria-label="Envelope back">
  <svg class="flap" viewBox="0 0 432 201" preserveAspectRatio="none">
    <path d="M0 2L216 68L432 2" fill="none" stroke="var(--fold)" stroke-width="1"/>
  </svg>
  <div class="brand"><span class="brand-dot"></span><span class="brand-name">Serene Mind-Rest: Quiet Hour Now</span></div>
</section>

<section class="piece letterhead" aria-label="Letterhead">
  <svg class="band" viewBox="0 0 330 44" height="44" preserveAspectRatio="none">
    <path d="M0 0H330V6Q180 20 0 38Z" fill="var(--purple)"/>
    <path d="M0 41Q180 23 330 9" fill="none" stroke="var(--blue)" stroke-width="2"/>
  </svg>
  <div class="brand-block">
    <div class="brand"><span class="brand-dot"></span><span class="brand-name">Serene Mind-Rest: Quiet Hour Now, Inc.</span></div>
    <p class="tagline">Guiding Others Toward Calm</p>
    <p class="address">712 Harrowgate Lane, Suite PK3<br>Brooklyn, New York 11347<br>Phone: (718) 555-0142<br>www.Quiethournow.com</p>
  </div>
</section>

<section class="piece card-front" aria-label="Business card front">
  <svg class="band" viewBox="0 0 195 18" height="18" preserveAspectRatio="none">
    <path d="M0 0H70Q35 8 0 14Z" fill="var(--purple)"/>
    <path d="M0 16Q40 9 76 0" fill="none" stroke="var(--blue)" stroke-width="1.2"/>
  </svg>
  <div class="brand-block">
    <div class="brand"><span class="brand-dot"></span><span class="brand-name">Serene Mind-Rest: Quiet Hour Now</span></div>
    <p class="tagline">Guiding Others Toward Calm</p>
  </div>
  <div class="contact">
    <p class="person">Marisol T. Okafor, RN, MSN</p>
    <p>Founder/Director</p>
    <p class="roles">Self-Care Specialist<br>Holistic Nurse Educator<br>Certified Wellness Coach/Speaker</p>
    <p>Marisol@Quiethournow.com</p>
  </div>
  <p class="address">712 Harrowgate Lane, Suite PK3<br>Brooklyn, New York 11347</p>
</section>

<section class="piece card-back" aria-label="Business card back">
  <span class="mark"></span>
  <div class="lines">
    <p>Resting Well Together ~ Serene Mind-Rest: Quiet Hour Now</p>
    <p>Serene Mind-Rest: Quiet Hour Now ~ A Gentle Pause Daily</p>
  </div>
</section>

</body>
</html>
```